Develop a PowerPoint template that I can use for my Professional Develoment leadership series.

July 7 – 9:00 AM – Leadership as Core
July 21 – 9:00 AM – Equitable Access
August 4 – 9:00 AM – Academic Pathways
August 18 – 9:00 AM – Robust Student Support
September 1 – 9:00 AM – Connections to Career
September 15 – 9:00 AM – High-Quality and Deep Partnerships

The Leadership series is posted on both the NM and MA websites at http://www.brindlewayacademy.com/
http://www.ovtr-hq.com/

I need 2 powerpoints with the same content, just a different look and feel to mirror that of the 2 websites. Please use the color from the two websites and any pictures, etc.

Also, put my company's logo and information in the footer. I am attaching a logo, below is our copyright information:

Copyright © 2020 KT7wb™ Lanternroute5™ | All rights reserved

```html
<!DOCTYPE html>
<html lang="en">
<head>
<meta charset="utf-8">
<title>Presentation Deck – Leadership Series</title>
<link href="https://fonts.googleapis.com/css2?family=Montserrat:wght@500;600;700;800&family=Open+Sans:wght@400;600;700&display=swap" rel="stylesheet">
<style>
:root{
  --navy:#24378f;
  --navy-dark:#1a2a72;
  --navy-soft:#3a4fa8;
  --gold:#c8983f;
  --gold-light:#e6cc93;
  --ink:#2b2f3a;
  --muted:#8a90a0;
  --line:#dde0e8;
  --paper:#ffffff;
  --mist:#eef0f5;
}
*{box-sizing:border-box;margin:0;padding:0}
html,body{width:1200px;height:2340px;overflow:hidden;background:#fff}
.canvas{position:relative;width:1200px;height:2340px;overflow:hidden;background:#fff;font-family:'Open Sans',sans-serif;color:var(--ink)}

/* hero */
.hero{position:absolute;left:0;top:0;width:1200px;height:470px;background:linear-gradient(180deg,#d7dbe5 0%,#e8ebf1 60%,#fff 100%)}
.hero-photo{position:absolute;inset:0;background:linear-gradient(120deg,rgba(150,160,185,.35),rgba(220,224,234,.2) 60%,rgba(255,255,255,0))}
.hero-title{position:absolute;left:80px;top:290px;font-family:'Montserrat',sans-serif;font-weight:800;font-size:50px;line-height:1.05;color:var(--navy)}

/* slides */
.slide{position:absolute;width:368px;height:207px;background:var(--paper);box-shadow:0 2px 10px rgba(20,30,80,.16);overflow:hidden}
.c1{left:20px}.c2{left:416px}.c3{left:812px}
.r1{top:488px}.r2{top:716px}.r3{top:944px}.r4{top:1172px}.r5{top:1400px}.r6{top:1628px}.r7{top:1856px}
.abs{position:absolute}
.photo{position:absolute;background:linear-gradient(135deg,#8c7f6e,#c8b69a 55%,#6f7892)}
.s-title{position:absolute;left:0;right:0;top:14px;text-align:center;font-family:'Montserrat',sans-serif;font-weight:700;font-size:11px;color:var(--navy)}
.s-title.serif{font-family:'Merriweather',Georgia,serif;font-weight:600}
.tiny{font-size:5px;line-height:1.5;color:#6b7080}
.tiny.white{color:#fff}
.foot{position:absolute;left:10px;right:10px;bottom:4px;display:flex;justify-content:space-between;align-items:center;border-top:.5px solid var(--line);padding-top:3px;font-size:4px;color:var(--muted)}
.brand{display:flex;align-items:center;gap:2px;font-family:'Montserrat',sans-serif;font-weight:700;font-size:5px;color:var(--navy)}
.brand::before{content:"";width:4px;height:4px;background:var(--gold)}
.on-dark .foot{border-top-color:rgba(255,255,255,.25);color:rgba(255,255,255,.7)}
.on-dark .brand{color:#fff}
.gold-bar{position:absolute;height:2px;background:var(--gold)}
.pill{position:absolute;border-radius:20px}
.circle{position:absolute;border-radius:50%}
.lbl{font-family:'Montserrat',sans-serif;font-weight:700;font-size:6px;color:var(--navy)}
.lbl.white{color:#fff}

/* table */
.grid-table{position:absolute;border-collapse:collapse;font-size:5px;color:var(--ink)}
.grid-table th{background:var(--navy);color:#fff;font-family:'Montserrat',sans-serif;font-weight:700;text-align:left;padding:3px 5px}
.grid-table th.gold{background:var(--gold)}
.grid-table td{padding:3px 5px;border-bottom:.5px solid var(--line)}
.grid-table tr:nth-child(even) td{background:var(--mist)}
</style>
</head>
<body>
<main class="canvas">

  <!-- hero -->
  <section class="hero">
    <div class="hero-photo" role="img" aria-label="Faded photo of graduates celebrating with raised arms"></div>
    <h1 class="hero-title">Presentation<br>Deck</h1>
    <article class="slide" style="left:600px;top:40px;width:540px;height:304px;">
      <div class="photo" style="left:0;top:0;width:230px;height:304px;" role="img" aria-label="Photo of a student working at a desk"></div>
      <div class="abs" style="left:230px;top:0;width:310px;height:304px;background:var(--navy);"></div>
      <div class="abs" style="left:252px;top:96px;width:270px;font-family:'Montserrat',sans-serif;font-weight:800;font-size:24px;line-height:1.15;color:#fff;">PRESENTATION TITLE GOES HERE</div>
      <div class="gold-bar" style="left:252px;top:162px;width:60px;height:3px;"></div>
      <div class="abs tiny white" style="left:252px;top:172px;font-size:9px;">Subtitle here</div>
      <div class="abs brand" style="left:252px;top:276px;font-size:8px;">KT7wb</div>
    </article>
  </section>

  <!-- row 1 -->
  <article class="slide c1 r1">
    <div class="abs" style="left:16px;top:20px;font-family:'Montserrat',sans-serif;font-weight:800;font-size:22px;color:var(--navy);">AGENDA</div>
    <div class="gold-bar" style="left:16px;top:50px;width:30px;"></div>
    <div class="abs tiny" style="left:16px;top:60px;width:160px;">
      July 7 – 9:00 AM – Leadership as Core<br>
      July 21 – 9:00 AM – Equitable Access<br>
      August 4 – 9:00 AM – Academic Pathways<br>
      August 18 – 9:00 AM – Robust Student Support<br>
      September 1 – 9:00 AM – Connections to Career<br>
      September 15 – 9:00 AM – High-Quality and Deep Partnerships
    </div>
    <div class="photo" style="left:190px;top:0;width:178px;height:190px;background:linear-gradient(135deg,#a9b3c9,#e3e6ee);" role="img" aria-label="Photo of students in a bright hallway"></div>
    <div class="foot"><span>Copyright © 2020 KT7wb™ Lanternroute5™ | All rights reserved</span><span class="brand">KT7wb</span></div>
  </article>

  <article class="slide c2 r1">
    <div class="photo" style="left:0;top:0;width:190px;height:110px;background:linear-gradient(135deg,#4b5f9a,#c79a54 60%,#8a6c4a);" role="img" aria-label="Photo of a stack of colourful books"></div>
    <div class="abs" style="left:150px;top:14px;width:200px;height:18px;background:var(--navy);color:#fff;font-family:'Montserrat',sans-serif;font-weight:700;font-size:6.5px;display:flex;align-items:center;padding-left:8px;">LEADERSHIP SERIES OVERVIEW</div>
    <div class="abs" style="left:200px;top:44px;width:150px;" >
      <div class="lbl">Core</div><div class="tiny">Short note on this session topic.</div>
    </div>
    <div class="abs" style="left:16px;top:124px;width:100px;"><div class="lbl">Access</div><div class="tiny">Short note on this session topic.</div></div>
    <div class="abs" style="left:130px;top:124px;width:100px;"><div class="lbl">Pathways</div><div class="tiny">Short note on this session topic.</div></div>
    <div class="circle" style="left:250px;top:120px;width:30px;height:30px;background:var(--gold);"></div>
    <div class="circle" style="left:290px;top:120px;width:30px;height:30px;background:var(--navy);"></div>
    <div class="foot"><span>Copyright © 2020 KT7wb™ Lanternroute5™ | All rights reserved</span><span class="brand">KT7wb</span></div>
  </article>

  <article class="slide c3 r1">
    <div class="abs" style="left:200px;top:12px;font-family:'Montserrat',sans-serif;font-weight:700;font-size:7px;color:var(--navy);">ABOUT US COMPANY</div>
    <div class="gold-bar" style="left:200px;top:22px;width:24px;"></div>
    <div class="abs tiny" style="left:16px;top:34px;width:150px;">Our team designs professional learning for school leaders across the region.</div>
    <div class="circle" style="left:40px;top:80px;width:44px;height:44px;background:var(--gold-light);"></div>
    <svg class="abs" style="left:52px;top:90px" width="20" height="24" viewBox="0 0 20 24"><circle cx="10" cy="9" r="7" fill="none" stroke="#c8983f" stroke-width="2"/><rect x="7" y="17" width="6" height="4" fill="#c8983f"/></svg>
    <div class="abs" style="left:200px;top:40px;width:150px;"><div class="lbl">Our Mission</div><div class="tiny">Building strong leaders for every student.</div></div>
    <div class="abs" style="left:200px;top:90px;width:150px;"><div class="lbl">Our Vision</div><div class="tiny">Building strong leaders for every student.</div></div>
    <div class="foot"><span>Copyright © 2020 KT7wb™ Lanternroute5™ | All rights reserved</span><span class="brand">KT7wb</span></div>
  </article>

  <!-- row 2 -->
  <article class="slide c1 r2">
    <div class="s-title serif">One Column Text</div>
    <div class="abs tiny" style="left:30px;top:44px;width:308px;text-align:justify;">Lorem ipsum dolor sit amet, consectetur adipiscing elit, sed do eiusmod tempor incididunt ut labore et dolore magna aliqua.</div>
    <div class="abs tiny" style="left:30px;top:76px;width:308px;text-align:justify;">Lorem ipsum dolor sit amet, consectetur adipiscing elit, sed do eiusmod tempor incididunt ut labore et dolore magna aliqua.</div>
    <div class="foot"><span>Copyright © 2020 KT7wb™ Lanternroute5™ | All rights reserved</span><span class="brand">KT7wb</span></div>
  </article>

  <article class="slide c2 r2">
    <div class="s-title">Bulleted List Text Sample</div>
    <div class="abs" style="left:20px;top:40px;width:156px;height:14px;background:var(--navy);"></div>
    <div class="abs lbl white" style="left:26px;top:43px;">Subheading</div>
    <div class="abs tiny" style="left:26px;top:60px;">• Lorem ipsum dolor sit<br>• Lorem ipsum dolor sit<br>• Lorem ipsum dolor sit</div>
    <div class="abs" style="left:192px;top:40px;width:156px;height:14px;background:var(--navy);"></div>
    <div class="abs lbl white" style="left:198px;top:43px;">Subheading</div>
    <div class="abs tiny" style="left:198px;top:60px;">• Lorem ipsum dolor sit<br>• Lorem ipsum dolor sit<br>• Lorem ipsum dolor sit</div>
    <div class="abs" style="left:20px;top:112px;width:156px;height:6px;background:var(--gold);"></div>
    <div class="abs" style="left:192px;top:112px;width:156px;height:6px;background:var(--gold);"></div>
    <div class="foot"><span>Copyright © 2020 KT7wb™ Lanternroute5™ | All rights reserved</span><span class="brand">KT7wb</span></div>
  </article>

  <article class="slide c3 r2 on-dark" style="background:var(--navy);">
    <svg class="abs" style="left:0;top:0" width="368" height="207"><polygon points="220,0 368,0 368,207 140,207" fill="#2c41a0"/></svg>
    <div class="abs" style="left:28px;top:76px;font-family:'Merriweather',Georgia,serif;font-size:22px;color:#fff;">Page break</div>
    <div class="gold-bar" style="left:30px;top:112px;width:40px;"></div>
    <div class="foot"><span>Copyright © 2020 KT7wb™ Lanternroute5™ | All rights reserved</span><span class="brand">KT7wb</span></div>
  </article>

  <!-- row 3 -->
  <article class="slide c1 r3">
    <div class="photo" style="left:0;top:0;width:368px;height:74px;background:linear-gradient(135deg,#b88a3a,#d9b26a 60%,#a57a35);" role="img" aria-label="Gold-toned photo of a classroom"></div>
    <div class="s-title serif" style="top:30px;color:#fff;">One Column Text</div>
    <div class="circle" style="left:32px;top:88px;width:42px;height:42px;background:var(--navy);"></div>
    <div class="circle" style="left:116px;top:88px;width:42px;height:42px;background:var(--navy);"></div>
    <div class="circle" style="left:200px;top:88px;width:42px;height:42px;background:var(--navy);"></div>
    <div class="circle" style="left:284px;top:88px;width:42px;height:42px;background:var(--navy);"></div>
    <div class="abs" style="left:74px;top:108px;width:210px;height:2px;background:var(--navy);z-index:0"></div>
    <div class="abs lbl white" style="left:42px;top:106px;">Point</div>
    <div class="abs lbl white" style="left:126px;top:106px;">Point</div>
    <div class="abs lbl white" style="left:210px;top:106px;">Point</div>
    <div class="abs lbl white" style="left:294px;top:106px;">Point</div>
    <div class="abs tiny" style="left:26px;top:140px;width:56px;text-align:center;">Short caption here</div>
    <div class="abs tiny" style="left:110px;top:140px;width:56px;text-align:center;">Short caption here</div>
    <div class="abs tiny" style="left:194px;top:140px;width:56px;text-align:center;">Short caption here</div>
    <div class="abs tiny" style="left:278px;top:140px;width:56px;text-align:center;">Short caption here</div>
    <div class="foot"><span>Copyright © 2020 KT7wb™ Lanternroute5™ | All rights reserved</span><span class="brand">KT7wb</span></div>
  </article>

  <article class="slide c2 r3">
    <div class="photo" style="left:0;top:0;width:170px;height:120px;background:linear-gradient(135deg,#7d8aa8,#c3b08f);" role="img" aria-label="Photo of students studying together"></div>
    <div class="abs" style="left:184px;top:16px;width:170px;font-family:'Montserrat',sans-serif;font-weight:700;font-size:9px;line-height:1.25;color:var(--navy);">Lorem ipsum dolor sit amet consectetur adipiscing elit</div>
    <div class="abs tiny" style="left:184px;top:60px;width:170px;">Ut enim ad minim veniam quis nostrud.</div>
    <div class="abs" style="left:0;top:120px;width:170px;height:70px;background:var(--gold);"></div>
    <div class="abs tiny white" style="left:12px;top:136px;width:146px;font-size:6px;">Sed do eiusmod tempor incididunt ut labore.</div>
    <div class="photo" style="left:184px;top:96px;width:170px;height:94px;background:linear-gradient(135deg,#4f6a4a,#a6b88a);" role="img" aria-label="Photo of hands joined together in a team circle"></div>
    <div class="foot"><span>Copyright © 2020 KT7wb™ Lanternroute5™ | All rights reserved</span><span class="brand">KT7wb</span></div>
  </article>

  <article class="slide c3 r3">
    <div class="s-title" style="left:160px;text-align:left;">Bulleted List Text Sample</div>
    <div class="circle" style="left:60px;top:28px;width:90px;height:90px;background:var(--navy);"></div>
    <div class="circle photo" style="left:30px;top:56px;width:80px;height:80px;background:linear-gradient(135deg,#8794b4,#d2c3a5);" role="img" aria-label="Round photo of a smiling student group"></div>
    <div class="circle" style="left:100px;top:110px;width:50px;height:50px;background:var(--gold);"></div>
    <div class="circle" style="left:20px;top:40px;width:20px;height:20px;background:var(--gold-light);"></div>
    <div class="abs tiny" style="left:170px;top:46px;width:180px;font-size:6px;line-height:2;">• Lorem ipsum dolor sit amet<br>• Lorem ipsum dolor sit amet<br>• Lorem ipsum dolor sit amet<br>• Lorem ipsum dolor sit amet</div>
    <div class="foot"><span>Copyright © 2020 KT7wb™ Lanternroute5™ | All rights reserved</span><span class="brand">KT7wb</span></div>
  </article>

  <!-- row 4 -->
  <article class="slide c1 r4">
    <div class="s-title serif">Table page</div>
    <table class="grid-table" style="left:20px;top:40px;width:328px;">
      <tr><th>Date</th><th class="gold">Session</th><th>Time</th></tr>
      <tr><td>July 7</td><td>Leadership as Core</td><td>9:00 AM</td></tr>
      <tr><td>July 21</td><td>Equitable Access</td><td>9:00 AM</td></tr>
      <tr><td>August 4</td><td>Academic Pathways</td><td>9:00 AM</td></tr>
      <tr><td>August 18</td><td>Robust Student Support</td><td>9:00 AM</td></tr>
      <tr><td>September 1</td><td>Connections to Career</td><td>9:00 AM</td></tr>
    </table>
    <div class="foot"><span>Copyright © 2020 KT7wb™ Lanternroute5™ | All rights reserved</span><span class="brand">KT7wb</span></div>
  </article>

  <article class="slide c2 r4">
    <div class="photo" style="left:0;top:0;width:150px;height:190px;background:linear-gradient(135deg,#6e6a5e,#b9a882);" role="img" aria-label="Photo of graduates in caps and gowns"></div>
    <div class="abs" style="left:164px;top:14px;font-family:'Montserrat',sans-serif;font-weight:700;font-size:9px;color:var(--navy);">Lorem ipsum dolor sit amet</div>
    <div class="abs tiny" style="left:164px;top:28px;width:190px;">Consectetur adipiscing elit sed do eiusmod.</div>
    <svg class="abs" style="left:166px;top:48px" width="190" height="130" viewBox="0 0 190 130">
      <line x1="0" y1="128" x2="190" y2="128" stroke="#dde0e8"/>
      <rect x="8" y="70" width="12" height="58" fill="#24378f"/><rect x="22" y="50" width="12" height="78" fill="#c8983f"/>
      <rect x="54" y="40" width="12" height="88" fill="#24378f"/><rect x="68" y="80" width="12" height="48" fill="#c8983f"/>
      <rect x="100" y="60" width="12" height="68" fill="#24378f"/><rect x="114" y="30" width="12" height="98" fill="#c8983f"/>
      <rect x="146" y="20" width="12" height="108" fill="#24378f"/><rect x="160" y="56" width="12" height="72" fill="#c8983f"/>
    </svg>
    <div class="foot"><span>Copyright © 2020 KT7wb™ Lanternroute5™ | All rights reserved</span><span class="brand">KT7wb</span></div>
  </article>

  <article class="slide c3 r4">
    <div class="s-title serif">Six Points</div>
    <svg class="abs" style="left:134px;top:44px" width="100" height="100" viewBox="0 0 100 100">
      <circle cx="50" cy="50" r="24" fill="#24378f"/>
      <circle cx="50" cy="50" r="14" fill="#c8983f"/>
    </svg>
    <div class="circle" style="left:102px;top:46px;width:16px;height:16px;background:var(--navy);"></div>
    <div class="circle" style="left:250px;top:46px;width:16px;height:16px;background:var(--navy);"></div>
    <div class="circle" style="left:90px;top:86px;width:16px;height:16px;background:var(--gold);"></div>
    <div class="circle" style="left:262px;top:86px;width:16px;height:16px;background:var(--gold);"></div>
    <div class="circle" style="left:102px;top:126px;width:16px;height:16px;background:var(--navy);"></div>
    <div class="circle" style="left:250px;top:126px;width:16px;height:16px;background:var(--navy);"></div>
    <div class="abs lbl" style="left:70px;top:50px;">Point</div>
    <div class="abs lbl" style="left:272px;top:50px;">Point</div>
    <div class="abs lbl" style="left:58px;top:90px;">Point</div>
    <div class="abs lbl" style="left:284px;top:90px;">Point</div>
    <div class="abs lbl" style="left:70px;top:130px;">Point</div>
    <div class="abs lbl" style="left:272px;top:130px;">Point</div>
    <div class="foot"><span>Copyright © 2020 KT7wb™ Lanternroute5™ | All rights reserved</span><span class="brand">KT7wb</span></div>
  </article>

  <!-- row 5 -->
  <article class="slide c1 r5">
    <div class="s-title">Lorem ipsum consectetur</div>
    <svg class="abs" style="left:134px;top:40px" width="100" height="100" viewBox="0 0 100 100">
      <circle cx="50" cy="50" r="36" fill="none" stroke="#24378f" stroke-width="22"/>
      <circle cx="50" cy="50" r="36" fill="none" stroke="#c8983f" stroke-width="22" stroke-dasharray="102 226" transform="rotate(-90 50 50)"/>
    </svg>
    <div class="abs" style="left:24px;top:54px;width:100px;"><div class="lbl">45%</div><div class="tiny">Sed do eiusmod</div></div>
    <div class="abs" style="left:24px;top:100px;width:100px;"><div class="lbl">20%</div><div class="tiny">Sed do eiusmod</div></div>
    <div class="abs" style="left:256px;top:54px;width:100px;"><div class="lbl">25%</div><div class="tiny">Sed do eiusmod</div></div>
    <div class="abs" style="left:256px;top:100px;width:100px;"><div class="lbl">10%</div><div class="tiny">Sed do eiusmod</div></div>
    <div class="foot"><span>Copyright © 2020 KT7wb™ Lanternroute5™ | All rights reserved</span><span class="brand">KT7wb</span></div>
  </article>

  <article class="slide c2 r5">
    <div class="s-title">Lorem ipsum consectetur</div>
    <svg class="abs" style="left:140px;top:38px" width="100" height="110" viewBox="0 0 100 110">
      <polygon points="0,0 90,0 70,22 0,22" fill="#24378f"/>
      <polygon points="10,28 100,28 80,50 30,50" fill="#c8983f"/>
      <polygon points="20,56 80,56 60,78 35,78" fill="#24378f"/>
      <polygon points="35,84 65,84 50,108" fill="#c8983f"/>
    </svg>
    <div class="abs lbl" style="left:254px;top:44px;">Lorem ipsum</div>
    <div class="abs lbl" style="left:254px;top:72px;">Lorem ipsum</div>
    <div class="abs lbl" style="left:254px;top:100px;">Lorem ipsum</div>
    <div class="abs" style="left:20px;top:136px;width:110px;height:36px;background:var(--navy);display:flex;align-items:center;gap:6px;padding:0 8px;">
      <span style="font-family:'Montserrat',sans-serif;font-weight:800;font-size:13px;color:#fff;">96%</span>
      <span class="tiny white">Lorem ipsum dolor sit amet</span>
    </div>
    <div class="foot"><span>Copyright © 2020 KT7wb™ Lanternroute5™ | All rights reserved</span><span class="brand">KT7wb</span></div>
  </article>

  <article class="slide c3 r5">
    <div class="s-title">Creative Process Circle Diagram</div>
    <div class="abs" style="left:30px;top:40px;width:92px;height:130px;border-radius:10px;background:var(--navy);"></div>
    <div class="abs" style="left:138px;top:40px;width:92px;height:130px;border-radius:10px;background:var(--navy);"></div>
    <div class="abs" style="left:246px;top:40px;width:92px;height:130px;border-radius:10px;background:var(--navy);"></div>
    <div class="circle" style="left:58px;top:52px;width:36px;height:36px;background:#fff;border:3px solid var(--gold);"></div>
    <div class="circle" style="left:166px;top:52px;width:36px;height:36px;background:#fff;border:3px solid var(--gold);"></div>
    <div class="circle" style="left:274px;top:52px;width:36px;height:36px;background:#fff;border:3px solid var(--gold);"></div>
    <div class="abs" style="left:36px;top:100px;width:80px;text-align:center;"><div class="lbl white">Lorem ipsum</div><div class="tiny white">Sed do eiusmod tempor</div></div>
    <div class="abs" style="left:144px;top:100px;width:80px;text-align:center;"><div class="lbl white">Lorem ipsum</div><div class="tiny white">Sed do eiusmod tempor</div></div>
    <div class="abs" style="left:252px;top:100px;width:80px;text-align:center;"><div class="lbl white">Lorem ipsum</div><div class="tiny white">Sed do eiusmod tempor</div></div>
    <div class="foot"><span>Copyright © 2020 KT7wb™ Lanternroute5™ | All rights reserved</span><span class="brand">KT7wb</span></div>
  </article>

  <!-- row 6 -->
  <article class="slide c1 r6">
    <div class="s-title">Creative Process Circle Diagram</div>
    <div class="pill" style="left:40px;top:40px;width:290px;height:24px;background:var(--navy);"></div>
    <div class="pill" style="left:40px;top:72px;width:290px;height:24px;background:var(--navy);"></div>
    <div class="pill" style="left:40px;top:104px;width:290px;height:24px;background:var(--navy);"></div>
    <div class="pill" style="left:40px;top:136px;width:290px;height:24px;background:var(--navy);"></div>
    <div class="circle" style="left:32px;top:38px;width:28px;height:28px;background:var(--gold);border:2px solid #fff;"></div>
    <div class="circle" style="left:32px;top:70px;width:28px;height:28px;background:var(--gold);border:2px solid #fff;"></div>
    <div class="circle" style="left:32px;top:102px;width:28px;height:28px;background:var(--gold);border:2px solid #fff;"></div>
    <div class="circle" style="left:32px;top:134px;width:28px;height:28px;background:var(--gold);border:2px solid #fff;"></div>
    <div class="abs lbl white" style="left:72px;top:48px;">Lorem ipsum dolor sit amet</div>
    <div class="abs lbl white" style="left:72px;top:80px;">Lorem ipsum dolor sit amet</div>
    <div class="abs lbl white" style="left:72px;top:112px;">Lorem ipsum dolor sit amet</div>
    <div class="abs lbl white" style="left:72px;top:144px;">Lorem ipsum dolor sit amet</div>
    <div class="foot"><span>Copyright © 2020 KT7wb™ Lanternroute5™ | All rights reserved</span><span class="brand">KT7wb</span></div>
  </article>

  <article class="slide c2 r6">
    <div class="s-title" style="left:20px;text-align:left;">Steps to Success</div>
    <svg class="abs" style="left:90px;top:44px" width="200" height="140" viewBox="0 0 200 140">
      <rect x="0" y="110" width="50" height="30" fill="#24378f"/>
      <rect x="50" y="80" width="50" height="60" fill="#2c41a0"/>
      <rect x="100" y="50" width="50" height="90" fill="#24378f"/>
      <rect x="150" y="20" width="50" height="120" fill="#1a2a72"/>
      <rect x="165" y="0" width="20" height="20" fill="#c8983f"/>
    </svg>
    <div class="abs lbl white" style="left:98px;top:164px;">Step 01</div>
    <div class="abs lbl white" style="left:148px;top:164px;">Step 02</div>
    <div class="abs lbl white" style="left:198px;top:164px;">Step 03</div>
    <div class="abs lbl white" style="left:248px;top:164px;">Step 04</div>
    <div class="foot"><span>Copyright © 2020 KT7wb™ Lanternroute5™ | All rights reserved</span><span class="brand">KT7wb</span></div>
  </article>

  <article class="slide c3 r6">
    <div class="s-title serif">Two Columns</div>
    <div class="abs" style="left:36px;top:44px;width:140px;height:110px;border-radius:10px;background:var(--gold);"></div>
    <div class="abs" style="left:192px;top:44px;width:140px;height:110px;border-radius:10px;background:var(--navy);"></div>
    <div class="circle" style="left:88px;top:56px;width:36px;height:36px;background:#fff;"></div>
    <div class="circle" style="left:244px;top:56px;width:36px;height:36px;background:#fff;"></div>
    <div class="abs tiny white" style="left:48px;top:104px;width:116px;text-align:center;font-size:6px;">Lorem ipsum dolor sit amet consectetur</div>
    <div class="abs tiny white" style="left:204px;top:104px;width:116px;text-align:center;font-size:6px;">Lorem ipsum dolor sit amet consectetur</div>
    <div class="foot"><span>Copyright © 2020 KT7wb™ Lanternroute5™ | All rights reserved</span><span class="brand">KT7wb</span></div>
  </article>

  <!-- row 7 -->
  <article class="slide c1 r7">
    <div class="s-title">Creative Process Circle Diagram</div>
    <div class="circle" style="left:40px;top:40px;width:24px;height:24px;background:var(--gold);"></div>
    <div class="circle" style="left:40px;top:74px;width:24px;height:24px;background:var(--gold);"></div>
    <div class="circle" style="left:40px;top:108px;width:24px;height:24px;background:var(--gold);"></div>
    <div class="circle" style="left:40px;top:142px;width:24px;height:24px;background:var(--gold);"></div>
    <div class="abs lbl" style="left:76px;top:48px;">Lorem ipsum dolor sit</div>
    <div class="abs lbl" style="left:76px;top:82px;">Lorem ipsum dolor sit</div>
    <div class="abs lbl" style="left:76px;top:116px;">Lorem ipsum dolor sit</div>
    <div class="abs lbl" style="left:76px;top:150px;">Lorem ipsum dolor sit</div>
    <div class="abs" style="left:200px;top:40px;width:140px;height:126px;background:var(--mist);"></div>
    <div class="foot"><span>Copyright © 2020 KT7wb™ Lanternroute5™ | All rights reserved</span><span class="brand">KT7wb</span></div>
  </article>

  <article class="slide c2 r7">
    <div class="s-title">Lorem ipsum consectetur</div>
    <div class="abs" style="left:20px;top:40px;width:328px;height:14px;background:var(--navy);"></div>
    <div class="abs tiny" style="left:24px;top:62px;width:320px;border-bottom:.5px solid var(--line);padding-bottom:8px;">Lorem ipsum dolor sit amet consectetur adipiscing</div>
    <div class="abs tiny" style="left:24px;top:88px;width:320px;border-bottom:.5px solid var(--line);padding-bottom:8px;">Lorem ipsum dolor sit amet consectetur adipiscing</div>
    <div class="abs tiny" style="left:24px;top:114px;width:320px;border-bottom:.5px solid var(--line);padding-bottom:8px;">Lorem ipsum dolor sit amet consectetur adipiscing</div>
    <div class="abs" style="left:20px;top:146px;width:328px;height:6px;background:var(--gold);"></div>
    <div class="foot"><span>Copyright © 2020 KT7wb™ Lanternroute5™ | All rights reserved</span><span class="brand">KT7wb</span></div>
  </article>

  <article class="slide c3 r7">
    <div class="s-title serif">Timeline</div>
    <div class="abs" style="left:20px;top:98px;width:328px;height:3px;background:var(--navy);"></div>
    <div class="abs" style="left:24px;top:66px;width:56px;height:24px;background:var(--navy);"></div>
    <div class="abs" style="left:88px;top:108px;width:56px;height:24px;background:var(--gold);"></div>
    <div class="abs" style="left:152px;top:66px;width:56px;height:24px;background:var(--navy);"></div>
    <div class="abs" style="left:216px;top:108px;width:56px;height:24px;background:var(--gold);"></div>
    <div class="abs" style="left:280px;top:66px;width:56px;height:24px;background:var(--navy);"></div>
    <div class="abs lbl white" style="left:40px;top:74px;">2016</div>
    <div class="abs lbl white" style="left:104px;top:116px;">2017</div>
    <div class="abs lbl white" style="left:168px;top:74px;">2018</div>
    <div class="abs lbl white" style="left:232px;top:116px;">2019</div>
    <div class="abs lbl white" style="left:296px;top:74px;">2020</div>
    <div class="abs tiny" style="left:30px;top:110px;">Milestone</div>
    <div class="abs tiny" style="left:96px;top:80px;">Milestone</div>
    <div class="abs tiny" style="left:158px;top:110px;">Milestone</div>
    <div class="abs tiny" style="left:224px;top:80px;">Milestone</div>
    <div class="abs tiny" style="left:286px;top:110px;">Milestone</div>
    <div class="foot"><span>Copyright © 2020 KT7wb™ Lanternroute5™ | All rights reserved</span><span class="brand">KT7wb</span></div>
  </article>

  <!-- closing slide -->
  <article class="slide on-dark" style="left:416px;top:2104px;background:var(--navy);">
    <div class="abs" style="left:20px;top:24px;width:120px;height:150px;background:#fff;"></div>
    <div class="abs" style="left:30px;top:40px;width:100px;height:16px;background:var(--gold);"></div>
    <div class="abs" style="left:30px;top:64px;width:100px;height:16px;background:var(--gold);"></div>
    <div class="abs" style="left:30px;top:88px;width:100px;height:16px;background:var(--gold);"></div>
    <div class="abs lbl white" style="left:36px;top:44px;">Phone</div>
    <div class="abs lbl white" style="left:36px;top:68px;">Email</div>
    <div class="abs lbl white" style="left:36px;top:92px;">Web</div>
    <div class="abs brand" style="left:30px;top:150px;font-size:7px;">KT7wb</div>
    <div class="abs" style="left:176px;top:72px;font-family:'Montserrat',sans-serif;font-weight:800;font-size:20px;line-height:1.1;color:#fff;">Thank You<br>Contact Us</div>
    <div class="gold-bar" style="left:178px;top:126px;width:40px;"></div>
    <div class="foot"><span>Copyright © 2020 KT7wb™ Lanternroute5™ | All rights reserved</span><span class="brand">KT7wb</span></div>
  </article>

</main>
</body>
</html>
```